TGV Electricial Contracting Services

Hi guys, after a design for my small electrical company, have logo design files to be incorporated into the layout, the basic concept is electrical contracting services for residential, commercial, industrial & data services, image is clean clear and strong,

Card format is to have a nice clean logo on front,with maybe the Residential – commercial – industrial - data, followed with licensed & insured, followed by contact details on backside of the card.

Target Market(s)

Residential, commercial, industrial sectors.

Industry/Entity Type

Electrical

Contact Information for Business Card

TGV logo,
Residential – commercial – industrial - data
REC: 57310
Email: tgv@wavolink.net.au
Phone: 0472 358 129

Requirements
Must have
• Clean & strong design.
Nice to have
• If possible, I would like the logo colours inverted so the text is orange and the background is black on the front of the card, then the backside of the card be the reverse colour
Should not have
• No Sparks, lightning bolts,

```html
<!DOCTYPE html>
<html lang="en">
<head>
<meta charset="utf-8">
<title>TGV Electricial Contracting Services – Business Card</title>
<link rel="stylesheet" href="https://fonts.googleapis.com/css2?family=Open+Sans:wght@300;400;700;800&display=swap">
<style>
  :root {
    --backdrop: #e9e9e9;
    --card-black: #111010;
    --brand-orange: #e8691f;
    --orange-deep: #d95d17;
    --orange-faint: rgba(255, 190, 140, 0.28);
    --arrow-brown: #3a1e10;
    --ink-black: #141210;
    --paper-white: #fbf3ec;
  }
  * { margin: 0; padding: 0; box-sizing: border-box; }
  html, body {
    width: 1200px;
    height: 900px;
    overflow: hidden;
    background: var(--backdrop);
    font-family: "Open Sans", Arial, sans-serif;
  }
  .card-sheet {
    position: absolute;
    inset: 0;
    display: flex;
    align-items: center;
    justify-content: center;
    gap: 40px;
  }
  .card {
    position: relative;
    width: 540px;
    height: 310px;
    overflow: hidden;
    box-shadow: 0 6px 18px rgba(0, 0, 0, 0.18);
  }

  /* Front */
  .card-front { background: var(--card-black); }
  .front-arrow {
    position: absolute;
    left: 30px;
    top: 216px;
    width: 470px;
    height: 44px;
  }
  .front-brand {
    position: absolute;
    left: 190px;
    top: 52px;
    color: var(--brand-orange);
    text-align: left;
  }
  .brand-mark {
    display: block;
    font-weight: 800;
    font-size: 82px;
    line-height: 0.9;
    letter-spacing: 1px;
  }
  .brand-name {
    display: block;
    font-weight: 800;
    font-size: 14px;
    line-height: 1.2;
    margin-top: 4px;
    letter-spacing: 0.2px;
  }
  .service-list {
    position: absolute;
    left: 30px;
    right: 30px;
    top: 186px;
    display: flex;
    justify-content: space-between;
    list-style: none;
    color: var(--brand-orange);
    font-weight: 300;
    font-size: 19px;
    letter-spacing: 0.6px;
  }

  /* Back */
  .card-back { background: var(--brand-orange); }
  .back-watermark {
    position: absolute;
    left: 10px;
    top: 8px;
    color: var(--orange-faint);
    font-weight: 800;
    font-size: 200px;
    line-height: 1;
    letter-spacing: 4px;
  }
  .back-brand {
    position: absolute;
    right: 70px;
    top: 118px;
    color: var(--ink-black);
  }
  .back-brand .brand-mark { font-size: 76px; }
  .back-brand .brand-name { font-size: 13px; }
  .contact-phone {
    position: absolute;
    left: 262px;
    top: 258px;
    display: flex;
    align-items: center;
    gap: 6px;
    color: var(--paper-white);
    font-size: 20px;
    font-weight: 400;
    letter-spacing: 0.5px;
  }
  .contact-phone svg { width: 16px; height: 16px; }
  .licence-number {
    position: absolute;
    right: 8px;
    bottom: 22px;
    transform-origin: right bottom;
    transform: rotate(-90deg) translateX(100%);
    color: var(--paper-white);
    font-size: 16px;
    letter-spacing: 0.6px;
    white-space: nowrap;
  }
</style>
</head>
<body>
  <main class="card-sheet">
    <section class="card card-front" aria-label="Card front">
      <svg class="front-arrow" viewBox="0 0 470 44" aria-hidden="true">
        <path d="M0 12 H440 V2 L470 22 L440 42 V32 H0 Z" fill="var(--arrow-brown)"/>
      </svg>
      <div class="front-brand">
        <span class="brand-mark">TGV</span>
        <span class="brand-name">Todd Grant Vale Electrical</span>
      </div>
      <ul class="service-list">
        <li>RESIDENTIAL</li>
        <li>COMMERCIAL</li>
        <li>INDUSTRIAL</li>
        <li>DATA</li>
      </ul>
    </section>

    <section class="card card-back" aria-label="Card back">
      <div class="back-watermark" aria-hidden="true">TGV</div>
      <div class="back-brand">
        <span class="brand-mark">TGV</span>
        <span class="brand-name">Todd Grant Vale Electrical</span>
      </div>
      <p class="contact-phone">
        <svg viewBox="0 0 16 16" aria-hidden="true">
          <circle cx="8" cy="8" r="7" fill="none" stroke="currentColor" stroke-width="1.2"/>
          <path d="M5.4 4.2 L6.8 5.8 L6 6.8 Q7 9 9.2 10 L10.2 9.2 L11.8 10.6 L10.8 11.8 Q6.4 11.4 4.2 5.2 Z" fill="currentColor"/>
        </svg>
        0472 358 129
      </p>
      <p class="licence-number">REC: 57310</p>
    </section>
  </main>
</body>
</html>
```